Creation of a construction/bricklaying business website

Following the template format of "Kestrow 2", the following content would need to be included:
1. Landing page with 3 tiles that go to their own pages.
- Landing page to include background photo and description of services offered.
2. 3 tiles to include:
a) "Contact Us For A Free Quote or Friendly Discussion" Form (middle tile)
b) Case Studies and Testimonials
c) Certifications and Professional Membership
- Design logo to be used from previous ArtQuorum project. Example of logo attached below, please access full JPG files from our account.

Target Market(s)

Prospective clients seeking construction work (bricklaying speciality)

Industry/Entity Type

Residential Construction

Coding

Coded - Design and coding required

Number of Pages Required

4 page

Font styles to use
Sans Serif

Colors

Designer to choose colors to be used in the design.

Requirements
Must have
• Following the template format of "Kestrow 2", the following content would need to be included:
• 1. Landing parent page with 3 tiles that go to the 3 child pages.
• - Landing page to include background photo and description of services offered.
• 2. 3 tiles to include:
• a) "Contact Us For A Free Quote or Friendly Discussion" Form (middle tile)
• b) Case Studies and Testimonials (first tile / left side)
• c) Certifications and Professional Memberships (third tile / right side) (This should include logos of the relevant organisations being displayed. Specifically GLW and the Keel Gate GLW).
• - Design logo to be used from previous ArtQuorum project. Example of logo attached below, please access full JPG files from our account.
Nice to have
• Sleek and modern feel.
• Approachable in terms of how people can contact the company for a quote.
• Traditional pictures to give credibility and comfort around choosing this company.
Should not have
• Cheesy pictures
• Over-complicated
• Simple to use
• Easy URL domain name

```html
<!DOCTYPE html>
<html lang="en">
<head>
<meta charset="utf-8">
<title>R.T. Hale Building Ltd — Website</title>
<link href="https://fonts.googleapis.com/css2?family=Montserrat:wght@400;600;700&family=Questrial&display=swap" rel="stylesheet">
<style>
:root{
  --stage:#eceef1;
  --white:#ffffff;
  --blue:#1f72b8;
  --blue-dark:#165a95;
  --ink:#1f2328;
  --muted:#6b7178;
  --line:#d7dbe0;
  --card:#eeeff1;
  --cert-bg:#d3eaf5;
  --footer:#2c2d30;
  --footer-deep:#1f2023;
  --badge-red:#c4232f;
  --hero-a:#16345e;
  --hero-b:#3f77b4;
  --hero-c:#0d1d36;
  --case-a:#5c6a78;
  --case-b:#2e3e52;
  --photo-a:#cfd6de;
  --photo-b:#8a98a8;
}
*{box-sizing:border-box;margin:0;padding:0}
html,body{width:1200px;height:3659px;overflow:hidden}
body{background:var(--stage);font-family:"Questrial",sans-serif;color:var(--ink);position:relative}
.site{position:absolute;background:var(--white);box-shadow:0 4px 18px rgba(0,0,0,.12)}
.site--desktop{left:49px;top:0;width:775px;height:1732px}
.site--mobile{left:883px;top:117px;width:263px;height:3409px}

.welcome-bar{text-align:center;font-size:9px;color:var(--muted);border-bottom:1px solid var(--line)}
.site--desktop .welcome-bar{height:29px;line-height:29px}
.site--mobile .welcome-bar{height:20px;line-height:20px;font-size:7px}

.brand{display:flex;align-items:center;justify-content:center;gap:6px;font-family:"Montserrat",sans-serif;font-weight:700;color:var(--blue)}
.brand__mark{width:12px;height:12px;background:var(--blue)}
.site-header{position:relative;display:flex;align-items:center;justify-content:center}
.site--desktop .site-header{height:88px}
.site--desktop .brand{font-size:24px}
.site--mobile .site-header{height:70px}
.site--mobile .brand{font-size:18px}

.search{display:flex;align-items:center;justify-content:space-between;border:1px solid var(--line);color:var(--muted);font-size:8px;padding:0 8px}
.site--desktop .search{position:absolute;right:22px;top:33px;width:150px;height:22px}
.search svg{width:9px;height:9px}

.main-nav{background:var(--blue);display:flex;justify-content:center;align-items:center;gap:38px;height:29px}
.main-nav a{color:var(--white);font-family:"Montserrat",sans-serif;font-size:8px;font-weight:600;text-decoration:none;letter-spacing:.4px}

.mobile-bar{display:flex;align-items:center;gap:6px;padding:0 8px;height:29px;border-top:1px solid var(--line)}
.mobile-bar .search{flex:1;height:19px}
.menu-toggle{width:20px;height:19px;background:var(--blue);display:flex;flex-direction:column;justify-content:center;gap:3px;padding:0 4px}
.menu-toggle span{height:2px;background:var(--white)}

.hero{position:relative;background:linear-gradient(135deg,var(--hero-c) 0%,var(--hero-a) 40%,var(--hero-b) 75%,var(--hero-a) 100%)}
.site--desktop .hero{height:281px}
.site--mobile .hero{height:305px}
.hero__arrow{position:absolute;top:50%;width:24px;height:24px;margin-top:-12px;border-radius:50%;background:var(--white);display:flex;align-items:center;justify-content:center}
.hero__arrow svg{width:10px;height:10px}
.hero__arrow--prev{left:14px}
.hero__arrow--next{right:14px}

.section-title{display:flex;align-items:center;gap:10px;font-family:"Montserrat",sans-serif;font-weight:700;text-transform:uppercase;letter-spacing:.6px}
.section-title::before,.section-title::after{content:"";flex:1;height:2px;background:var(--blue)}
.site--desktop .section-title{font-size:13px;margin:0 auto;width:520px}
.site--mobile .section-title{font-size:11px;margin:0 14px}

.services{text-align:center}
.site--desktop .services{height:171px;padding-top:22px}
.site--desktop .services__grid{display:flex;justify-content:center;gap:34px;margin-top:18px}
.service{display:flex;flex-direction:column;align-items:center}
.service svg{width:40px;height:40px}
.service__label{font-family:"Montserrat",sans-serif;font-weight:700;font-size:7px;text-transform:uppercase;margin-top:8px;padding-bottom:5px;border-bottom:2px solid var(--ink);min-width:56px}
.site--mobile .services{padding:22px 0 0}
.site--mobile .services__grid{display:flex;flex-direction:column;align-items:center;gap:40px;margin-top:30px}
.site--mobile .service svg{width:44px;height:44px}

.cases{display:flex}
.site--desktop .cases{margin:27px 105px 0;height:192px}
.site--mobile .cases{flex-direction:column;height:407px}
.case{flex:1;position:relative;display:flex;flex-direction:column;align-items:center;justify-content:center;color:var(--white);text-align:center}
.case--one{background:linear-gradient(180deg,var(--case-a),var(--case-b))}
.case--two{background:linear-gradient(180deg,#6f8aa3,#2f4c67)}
.case__kicker{font-size:7px;letter-spacing:1px;text-transform:uppercase}
.case__title{font-family:"Montserrat",sans-serif;font-weight:700;font-size:11px;text-transform:uppercase;margin:4px 0 10px}
.btn{display:inline-block;font-family:"Montserrat",sans-serif;font-weight:700;font-size:6px;text-transform:uppercase;padding:4px 8px}
.btn--ghost{border:1px solid var(--white);color:var(--white)}
.btn--dark{background:var(--ink);color:var(--white)}

.testimonials .cards{display:flex}
.site--desktop .testimonials{padding-top:26px;height:214px}
.site--desktop .testimonials .cards{justify-content:center;gap:8px;margin-top:12px}
.site--desktop .card{width:160px}
.card__photo{background:linear-gradient(160deg,var(--photo-a),var(--photo-b))}
.site--desktop .card__photo{height:88px}
.card__body{background:var(--card);padding:8px 6px 10px}
.card__title{font-family:"Montserrat",sans-serif;font-weight:600;font-size:8px;margin-bottom:6px}
.site--mobile .testimonials{padding:26px 0 0;height:618px}
.site--mobile .testimonials .cards{flex-direction:column;align-items:center;gap:22px;margin-top:22px}
.site--mobile .card{width:170px}
.site--mobile .card__photo{height:100px}

.contact .fields{display:flex}
.field{border:1px solid var(--line);height:22px;font-size:7px;color:var(--muted);padding:0 6px;display:flex;align-items:center}
.site--desktop .contact{padding-top:30px;height:146px;text-align:center}
.site--desktop .contact .fields{justify-content:center;gap:10px;margin-top:14px}
.site--desktop .field{width:110px}
.submit{display:inline-block;font-family:"Montserrat",sans-serif;font-weight:700;font-size:6px;text-transform:uppercase;border:1px solid var(--line);padding:4px 12px;margin-top:10px}
.site--mobile .contact{padding:22px 0 0;height:268px;text-align:center}
.site--mobile .contact .fields{flex-direction:column;gap:10px;margin:18px 14px 0}

.cert{background:var(--cert-bg);text-align:center}
.site--desktop .cert{margin:8px 105px 0;height:273px;padding:22px 22px 0}
.site--mobile .cert{height:403px;padding:22px 12px 0}
.cert p{font-size:7px;line-height:1.45;margin:12px auto 0;max-width:480px}
.cert__note{color:var(--blue);font-size:7px;font-weight:600;margin-top:10px}
.pills{display:flex;flex-wrap:wrap;justify-content:center;gap:6px;margin-top:10px}
.pill{background:var(--white);font-size:6px;padding:4px 8px;font-family:"Montserrat",sans-serif;font-weight:600}
.pill--active{background:var(--blue-dark);color:var(--white)}
.site--mobile .pills{flex-direction:column;align-items:center;gap:7px}
.badges{display:flex;justify-content:center;gap:22px;margin-top:14px}
.badge{display:flex;gap:3px;background:var(--white);padding:4px}
.badge span{width:26px;height:28px;background:var(--badge-red)}
.badge--solo span{width:40px}

.footer{background:var(--footer);color:#c9ccd1}
.footer h4{font-family:"Montserrat",sans-serif;font-weight:600;color:var(--white);font-size:9px}
.subscribe{display:flex;flex-direction:column;align-items:center}
.subscribe__form{display:flex;margin-top:8px}
.subscribe__input{height:18px;border:1px solid #555;font-size:6px;padding:0 6px;display:flex;align-items:center;color:#999}
.subscribe__btn{height:18px;background:var(--footer-deep);color:var(--white);font-size:6px;padding:0 10px;display:flex;align-items:center;border:1px solid #555;font-family:"Montserrat",sans-serif;font-weight:700}
.footer__col{font-size:6.5px;line-height:1.7}
.footer__col h4{margin-bottom:6px}
.info-line{display:flex;align-items:center;gap:4px}
.info-line svg{width:7px;height:7px;flex:none}
.site--desktop .footer{height:214px;padding-top:30px}
.site--desktop .subscribe__input{width:150px}
.site--desktop .footer__cols{display:flex;justify-content:center;gap:70px;margin-top:20px}
.site--desktop .footer__col{width:150px}
.site--desktop .footer__col--center{text-align:center}
.nav-cols{display:flex;gap:26px;justify-content:center}
.site--mobile .footer{height:415px;padding-top:28px;text-align:center}
.site--mobile .subscribe__input{width:140px}
.site--mobile .footer__col{margin-top:26px}
.site--mobile .info-line{justify-content:center}

.legal{background:var(--footer-deep);color:#9ea2a8;font-size:6.5px;display:flex;align-items:center}
.socials{display:flex;gap:4px}
.socials span{width:11px;height:11px;border-radius:50%;background:var(--white)}
.site--desktop .legal{height:25px;justify-content:space-between;padding:0 22px}
.site--mobile .legal{height:61px;flex-direction:column;justify-content:center;gap:8px}
</style>
</head>
<body>

<svg width="0" height="0" style="position:absolute" aria-hidden="true">
  <defs>
    <symbol id="i-extension" viewBox="0 0 40 40"><rect x="6" y="8" width="12" height="28" fill="#1f72b8"/><rect x="20" y="16" width="14" height="20" fill="#1f72b8"/><g fill="#fff"><rect x="9" y="12" width="2" height="2"/><rect x="13" y="12" width="2" height="2"/><rect x="9" y="18" width="2" height="2"/><rect x="13" y="18" width="2" height="2"/><rect x="9" y="24" width="2" height="2"/><rect x="13" y="24" width="2" height="2"/><rect x="24" y="21" width="2" height="2"/><rect x="28" y="21" width="2" height="2"/><rect x="24" y="27" width="2" height="2"/><rect x="28" y="27" width="2" height="2"/></g></symbol>
    <symbol id="i-newbuild" viewBox="0 0 40 40"><path d="M4 20 L20 6 L36 20 L32 20 L32 35 L8 35 L8 20 Z" fill="#1f72b8"/><rect x="17" y="24" width="6" height="11" fill="#fff"/></symbol>
    <symbol id="i-wall" viewBox="0 0 40 40"><rect x="4" y="8" width="32" height="26" fill="#1f72b8"/><g stroke="#fff" stroke-width="1.5"><line x1="4" y1="14.5" x2="36" y2="14.5"/><line x1="4" y1="21" x2="36" y2="21"/><line x1="4" y1="27.5" x2="36" y2="27.5"/><line x1="14" y1="8" x2="14" y2="14.5"/><line x1="26" y1="8" x2="26" y2="14.5"/><line x1="20" y1="14.5" x2="20" y2="21"/><line x1="9" y1="14.5" x2="9" y2="21"/><line x1="31" y1="14.5" x2="31" y2="21"/><line x1="14" y1="21" x2="14" y2="27.5"/><line x1="26" y1="21" x2="26" y2="27.5"/><line x1="20" y1="27.5" x2="20" y2="34"/></g></symbol>
    <symbol id="i-plaster" viewBox="0 0 40 40"><path d="M4 30 L26 18 L34 24 L12 36 Z" fill="#1f72b8"/><rect x="22" y="6" width="3" height="14" transform="rotate(-30 23 13)" fill="#1f72b8"/></symbol>
    <symbol id="i-brick" viewBox="0 0 40 40"><rect x="6" y="22" width="12" height="6" fill="#1f72b8"/><rect x="20" y="22" width="12" height="6" fill="#1f72b8"/><rect x="12" y="30" width="12" height="6" fill="#1f72b8"/><rect x="13" y="14" width="12" height="6" fill="#1f72b8"/><path d="M26 4 L34 10 L30 14 L24 9 Z" fill="#1f72b8"/></symbol>
    <symbol id="i-ground" viewBox="0 0 40 40"><rect x="4" y="32" width="32" height="4" fill="#1f72b8"/><rect x="12" y="22" width="16" height="9" fill="#1f72b8"/><rect x="15" y="13" width="10" height="8" fill="#1f72b8"/><rect x="18" y="4" width="4" height="8" fill="#1f72b8"/></symbol>
    <symbol id="i-search" viewBox="0 0 10 10"><circle cx="4" cy="4" r="3" fill="none" stroke="#6b7178" stroke-width="1.3"/><line x1="6.3" y1="6.3" x2="9.3" y2="9.3" stroke="#6b7178" stroke-width="1.3"/></symbol>
    <symbol id="i-pin" viewBox="0 0 10 10"><path d="M5 0 C2.2 0 1 2 1 3.8 C1 6.5 5 10 5 10 C5 10 9 6.5 9 3.8 C9 2 7.8 0 5 0 Z" fill="#1f72b8"/><circle cx="5" cy="3.8" r="1.4" fill="#2c2d30"/></symbol>
    <symbol id="i-phone" viewBox="0 0 10 10"><path d="M2 0.5 L4 2.5 L3 4 C3.8 5.6 4.4 6.2 6 7 L7.5 6 L9.5 8 L8 9.5 C4 9 1 6 0.5 2 Z" fill="#1f72b8"/></symbol>
    <symbol id="i-mail" viewBox="0 0 10 10"><rect x="0.5" y="2" width="9" height="6" fill="#1f72b8"/><path d="M0.5 2 L5 5.5 L9.5 2" fill="none" stroke="#2c2d30" stroke-width="0.8"/></symbol>
    <symbol id="i-prev" viewBox="0 0 10 10"><path d="M6.5 1.5 L3 5 L6.5 8.5" fill="none" stroke="#1f2328" stroke-width="1.6"/></symbol>
    <symbol id="i-next" viewBox="0 0 10 10"><path d="M3.5 1.5 L7 5 L3.5 8.5" fill="none" stroke="#1f2328" stroke-width="1.6"/></symbol>
  </defs>
</svg>

<!-- Desktop layout -->
<div class="site site--desktop">
  <div class="welcome-bar">Welcome To The R.T. Hale Building LTD</div>
  <header class="site-header">
    <div class="brand"><span class="brand__mark"></span>R.T. Hale</div>
    <div class="search"><span>Search</span><svg><use href="#i-search"/></svg></div>
  </header>
  <nav class="main-nav">
    <a href="#">CONTACT US</a><a href="#">CASE STUDIES</a><a href="#">TESTIMONIALS</a><a href="#">CERTIFICATIONS</a><a href="#">MEMBERSHIP</a>
  </nav>
  <section class="hero" role="img" aria-label="Photo of a businessman sketching a glowing city skyline in front of him">
    <span class="hero__arrow hero__arrow--prev"><svg><use href="#i-prev"/></svg></span>
    <span class="hero__arrow hero__arrow--next"><svg><use href="#i-next"/></svg></span>
  </section>

  <section class="services">
    <h2 class="section-title">R.T. Hale Services</h2>
    <div class="services__grid">
      <div class="service"><svg><use href="#i-extension"/></svg><span class="service__label">Extensions</span></div>
      <div class="service"><svg><use href="#i-newbuild"/></svg><span class="service__label">New Build</span></div>
      <div class="service"><svg><use href="#i-wall"/></svg><span class="service__label">Garden Wall</span></div>
      <div class="service"><svg><use href="#i-plaster"/></svg><span class="service__label">Plastering</span></div>
      <div class="service"><svg><use href="#i-brick"/></svg><span class="service__label">Brickwork</span></div>
      <div class="service"><svg><use href="#i-ground"/></svg><span class="service__label">Groundwork</span></div>
    </div>
  </section>

  <section class="cases">
    <div class="case case--one" role="img" aria-label="Photo of a modern house with a timber deck at dusk">
      <span class="case__kicker">Case Studies - 1</span><span class="case__title">Lorem Ipsum Dolor Sit Amet</span><span class="btn btn--ghost">Read More</span>
    </div>
    <div class="case case--two" role="img" aria-label="Photo of a modern white house beside a swimming pool">
      <span class="case__kicker">Case Studies - 2</span><span class="case__title">Lorem Ipsum Dolor Sit Amet</span><span class="btn btn--ghost">Read More</span>
    </div>
  </section>

  <section class="testimonials">
    <h2 class="section-title">Testimonials</h2>
    <div class="cards">
      <article class="card"><div class="card__photo" role="img" aria-label="Photo of a smiling team of office colleagues"></div><div class="card__body"><div class="card__title">Lorem Ipsum Dolor Sit Amet</div><span class="btn btn--dark">Read More</span></div></article>
      <article class="card"><div class="card__photo" role="img" aria-label="Photo of a client working at a laptop"></div><div class="card__body"><div class="card__title">Lorem Ipsum Dolor Sit Amet</div><span class="btn btn--dark">Read More</span></div></article>
      <article class="card"><div class="card__photo" role="img" aria-label="Photo of colleagues in a meeting"></div><div class="card__body"><div class="card__title">Lorem Ipsum Dolor Sit Amet</div><span class="btn btn--dark">Read More</span></div></article>
    </div>
  </section>

  <section class="contact">
    <h2 class="section-title">Contact Us</h2>
    <div class="fields"><span class="field">Name*</span><span class="field">Email*</span><span class="field">Phone number*</span><span class="field">Description*</span></div>
    <span class="submit">Submit</span>
  </section>

  <section class="cert">
    <h2 class="section-title" style="width:auto">Certification &amp; Membership</h2>
    <p>R.T. Hale Building Ltd is a registered company with the Guild of Local Wallers. The GLW has a strict membership criteria &amp; dispute resolution service which gives our clients the confidence to entrust their residential building requirements with R.T. Hale Building.</p>
    <div class="cert__note">GLW Membership means that R.T. Hale Building Ltd:</div>
    <div class="pills">
      <span class="pill pill--active">Has a minimum of twelve months trading</span>
      <span class="pill">Have provided a professional reference</span>
      <span class="pill">Confirmation of business address</span>
      <span class="pill">Have provided a professional reference</span>
      <span class="pill">Confirmation of business address</span>
    </div>
    <div class="badges">
      <div class="badge" role="img" aria-label="Keel Gate GLW badges"><span></span><span></span></div>
      <div class="badge badge--solo" role="img" aria-label="Guild of Local Wallers badge"><span></span></div>
    </div>
  </section>

  <footer class="footer">
    <div class="subscribe"><h4>Subscribe Here</h4><div class="subscribe__form"><span class="subscribe__input">Email</span><span class="subscribe__btn">SUBSCRIBE</span></div></div>
    <div class="footer__cols">
      <div class="footer__col">
        <h4 style="text-align:center">Head Office</h4>
        <div class="info-line"><svg><use href="#i-pin"/></svg>Unit 4, Mill Lane, Harwick HX2 7QT</div>
        <div class="info-line"><svg><use href="#i-phone"/></svg>01632 960 418</div>
        <div class="info-line"><svg><use href="#i-mail"/></svg>info@rthalebuilding.example</div>
      </div>
      <div class="footer__col footer__col--center">
        <h4>Navigation</h4>
        <div class="nav-cols"><div>Contact Us<br>Case Studies<br>Testimonials</div><div>Certification<br>Membership</div></div>
      </div>
      <div class="footer__col footer__col--center">
        <h4>About Us</h4>
        <div>We build extensions, new homes and garden walls with care across the county, on time and on budget.</div>
      </div>
    </div>
  </footer>
  <div class="legal"><span>Copyright ©2018 R.T. Hale Building. All rights are Reserved.</span><span class="socials"><span></span><span></span><span></span><span></span><span></span><span></span></span></div>
</div>

<!-- Mobile layout -->
<div class="site site--mobile">
  <div class="welcome-bar">Welcome To The R.T. Hale Building LTD</div>
  <header class="site-header"><div class="brand"><span class="brand__mark"></span>R.T. Hale</div></header>
  <div class="mobile-bar"><div class="search"><span>Search</span><svg><use href="#i-search"/></svg></div><span class="menu-toggle"><span></span><span></span><span></span></span></div>
  <section class="hero" role="img" aria-label="Photo of a businessman sketching a glowing city skyline in front of him"></section>

  <section class="services">
    <h2 class="section-title">R.T. Hale Services</h2>
    <div class="services__grid">
      <div class="service"><svg><use href="#i-extension"/></svg><span class="service__label">Extensions</span></div>
      <div class="service"><svg><use href="#i-newbuild"/></svg><span class="service__label">New Build</span></div>
      <div class="service"><svg><use href="#i-wall"/></svg><span class="service__label">Garden Wall</span></div>
      <div class="service"><svg><use href="#i-plaster"/></svg><span class="service__label">Plastering</span></div>
      <div class="service"><svg><use href="#i-brick"/></svg><span class="service__label">Brickwork</span></div>
      <div class="service"><svg><use href="#i-ground"/></svg><span class="service__label">Groundwork</span></div>
    </div>
  </section>

  <section class="cases" style="margin-top:38px">
    <div class="case case--one" role="img" aria-label="Photo of a modern house with a timber deck at dusk">
      <span class="case__kicker">Case Studies - 1</span><span class="case__title">Lorem Ipsum Dolor Sit Amet</span><span class="btn btn--ghost">Read More</span>
    </div>
    <div class="case case--two" role="img" aria-label="Photo of a modern white house beside a swimming pool">
      <span class="case__kicker">Case Studies - 2</span><span class="case__title">Lorem Ipsum Dolor Sit Amet</span><span class="btn btn--ghost">Read More</span>
    </div>
  </section>

  <section class="testimonials">
    <h2 class="section-title">Testimonials</h2>
    <div class="cards">
      <article class="card"><div class="card__photo" role="img" aria-label="Photo of a smiling team of office colleagues"></div><div class="card__body"><div class="card__title">Lorem Ipsum Dolor Sit Amet</div><span class="btn btn--dark">Read More</span></div></article>
      <article class="card"><div class="card__photo" role="img" aria-label="Photo of a client working at a laptop"></div><div class="card__body"><div class="card__title">Lorem Ipsum Dolor Sit Amet</div><span class="btn btn--dark">Read More</span></div></article>
      <article class="card"><div class="card__photo" role="img" aria-label="Photo of colleagues in a meeting"></div><div class="card__body"><div class="card__title">Lorem Ipsum Dolor Sit Amet</div><span class="btn btn--dark">Read More</span></div></article>
    </div>
  </section>

  <section class="contact">
    <h2 class="section-title">Contact Us</h2>
    <div class="fields"><span class="field">Name*</span><span class="field">Email*</span><span class="field">Phone number*</span><span class="field">Description*</span></div>
    <span class="submit">Submit</span>
  </section>

  <section class="cert">
    <h2 class="section-title" style="margin:0">Certification &amp; Membership</h2>
    <p>R.T. Hale Building Ltd is a registered company with the Guild of Local Wallers. The GLW has a strict membership criteria &amp; dispute resolution service which gives our clients the confidence to entrust their residential building requirements with R.T. Hale Building.</p>
    <div class="cert__note">GLW Membership means that R.T. Hale Building Ltd:</div>
    <div class="pills">
      <span class="pill pill--active">Has a minimum of twelve months trading</span>
      <span class="pill">Have provided a professional reference</span>
      <span class="pill">Confirmation of business address</span>
      <span class="pill">Have provided a professional reference</span>
      <span class="pill">Confirmation of business address</span>
    </div>
    <div class="badges">
      <div class="badge" role="img" aria-label="Keel Gate GLW badges"><span></span><span></span></div>
      <div class="badge badge--solo" role="img" aria-label="Guild of Local Wallers badge"><span></span></div>
    </div>
  </section>

  <footer class="footer">
    <div class="subscribe"><h4>Subscribe Here</h4><div class="subscribe__form"><span class="subscribe__input">Email</span><span class="subscribe__btn">SUBSCRIBE</span></div></div>
    <div class="footer__col">
      <h4>Head Office</h4>
      <div class="info-line"><svg><use href="#i-pin"/></svg>Unit 4, Mill Lane, Harwick HX2 7QT</div>
      <div class="info-line"><svg><use href="#i-phone"/></svg>01632 960 418</div>
      <div class="info-line"><svg><use href="#i-mail"/></svg>info@rthalebuilding.example</div>
    </div>
    <div class="footer__col">
      <h4>Navigation</h4>
      <div>Contact Us<br>Case Studies<br>Testimonials<br>Certification<br>Membership</div>
    </div>
    <div class="footer__col">
      <h4>About Us</h4>
      <div>We build extensions, new homes and<br>garden walls with care across the county,<br>on time and on budget.</div>
    </div>
  </footer>
  <div class="legal"><span>Copyright ©2018 R.T. Hale Building. All rights are Reserved.</span><span class="socials"><span></span><span></span><span></span><span></span><span></span><span></span></span></div>
</div>

</body>
</html>
```